BLENOX - Joining Study and Progress for Fair Opportunity

Brochure is needed for the European Project "BLENOX". We will distribute this flyer during conferences and events to our audiences (mainly academics, researchers, business individuals, policy makers and members of civil society groups) in order to provide the basic information about the project.
The main scope of the project is to support research organisations across Europe to design and implement gender equality plans in order to promote the women’s position of the filed of STEM research.

We are providing a video to explain the layout: https://www.vidstreamhub.example/watch?v=Xk4pR9tLm2Z.
We think size can range from A4-A3.

We are attaching files to provide with concrete information on our requirements:
- BLENOX Brochure Layout_SA.ppt: includes the content we would like to include in the flyer. There is also the URL to the project website
- blenox Logo.zip: the project logo
- Partners Logos.zip: the Logos that will be included
We would like to use colours that belong to the project logo colour range. Regarding the images that you may include in the flyer, we wouldn't like to propose any because we do not want to limitate your imagination. We have some at the website https://blenox-project.example/. They could be diverse (age, race, gender, etc.) relevant to women and men.

```html
<!DOCTYPE html>
<html lang="en">
<head>
<meta charset="utf-8">
<title>BLENOX Brochure</title>
<link href="https://fonts.googleapis.com/css2?family=Montserrat:wght@600;700;800&family=Open+Sans:wght@400;600&display=swap" rel="stylesheet">
<style>
:root{
  --purple:#4b3f9c;
  --purple-dark:#372c7d;
  --yellow:#f6b222;
  --white:#ffffff;
  --ink:#2b2b3a;
  --paper:#ecebe7;
  --flag:#1f3f9a;
  --badge-a:#d9d7e6;
  --badge-b:#e6e1f2;
}
*{box-sizing:border-box;margin:0;padding:0}
html,body{width:1200px;height:1200px;overflow:hidden}
body{background:var(--paper);font-family:"Open Sans",Arial,sans-serif;color:var(--ink)}
.sheet{position:absolute;left:188px;top:22px;display:grid;grid-template-columns:400px 400px;gap:24px}
.page{position:relative;width:400px;height:566px;overflow:hidden;background:var(--white);box-shadow:0 2px 8px rgba(0,0,0,.12)}
.photo{position:absolute}
.tone-lab{background:
  radial-gradient(circle at 30% 35%,rgba(232,196,170,.85) 0 14%,transparent 34%),
  radial-gradient(circle at 72% 60%,rgba(255,255,255,.7) 0 12%,transparent 36%),
  linear-gradient(135deg,#5c6b8e 0%,#a9b4c9 40%,#d7d1c6 62%,#4d5778 100%)}
.tone-warm{background:
  radial-gradient(circle at 40% 40%,rgba(196,140,108,.9) 0 16%,transparent 40%),
  linear-gradient(135deg,#7d5c4c 0%,#d9bfa4 45%,#f1e7da 65%,#6e6272 100%)}
.tone-cool{background:
  radial-gradient(circle at 65% 55%,rgba(214,170,140,.8) 0 12%,transparent 32%),
  linear-gradient(160deg,#3e4e78 0%,#9fb0cf 45%,#e6eaf2 62%,#414b6d 100%)}
.tone-desk{background:
  radial-gradient(circle at 30% 40%,rgba(246,178,34,.55) 0 10%,transparent 28%),
  radial-gradient(circle at 70% 65%,rgba(75,63,156,.45) 0 12%,transparent 30%),
  linear-gradient(135deg,#a59c8e 0%,#efe8dc 50%,#8f8678 100%)}
.deco{position:absolute;left:0;top:0}
.brand{position:absolute;display:flex;align-items:center;gap:7px;font-family:"Montserrat",sans-serif;font-weight:800;color:var(--purple);letter-spacing:.04em}
.brand .dot{width:14px;height:14px;border-radius:50%;background:var(--yellow)}
.h-title{font-family:"Montserrat",sans-serif;font-weight:800;text-transform:uppercase;line-height:1.12}
.h-sec{font-family:"Montserrat",sans-serif;font-weight:700;text-transform:uppercase;font-size:10.5px;letter-spacing:.03em}
.copy{font-size:7.4px;line-height:1.5}
.funding{position:absolute;display:flex;align-items:center;gap:7px;font-size:5.6px;line-height:1.35}
.funding .flag{width:30px;height:20px;background:var(--flag);flex:none}
/* cover */
.cover .title{position:absolute;left:34px;top:398px;width:330px;font-size:22px;color:var(--purple)}
/* page 2 */
.about{position:absolute;left:0;top:208px;width:400px;height:104px;background:var(--purple);padding:16px 26px;color:var(--white)}
.about .h-sec{color:var(--yellow);margin-bottom:6px}
.consortium{position:absolute;left:0;top:312px;width:400px;padding:14px 26px}
.consortium .h-sec{color:var(--purple);margin-bottom:5px}
.badges{display:flex;flex-wrap:wrap;gap:7px;margin-top:9px}
.badges span{width:48px;height:16px;border-radius:3px;background:var(--badge-a)}
.badges span:nth-child(even){background:var(--badge-b)}
.goal{position:absolute;left:200px;top:438px;width:200px;height:128px;background:var(--purple);color:var(--white);padding:16px 18px}
.goal .h-sec{color:var(--yellow);margin-bottom:5px}
.goal-strip{position:absolute;left:0;top:432px;width:400px;height:6px;background:var(--yellow)}
/* inside */
.hubs{position:absolute;left:20px;top:24px;width:168px}
.hubs .h-sec{color:var(--purple);font-size:11.5px;line-height:1.2;margin-bottom:8px}
.impact{position:absolute;left:20px;top:214px;width:168px}
.impact .h-sec{color:var(--purple);margin-bottom:5px}
.levels-head{position:absolute;left:0;top:316px;width:400px;height:24px;background:var(--purple);color:var(--yellow);padding:6px 20px}
.levels{position:absolute;left:0;top:340px;width:400px;height:124px;background:var(--yellow);padding:10px 20px;list-style:none;display:grid;grid-template-columns:1fr 1fr;gap:10px 14px}
.levels li{display:flex;align-items:center;gap:8px;font-size:7.4px;line-height:1.35;font-weight:600;color:var(--purple-dark)}
.levels .ico{flex:none;width:28px;height:28px;border-radius:50%;background:var(--purple);display:flex;align-items:center;justify-content:center}
.phases{position:absolute;left:180px;top:464px;width:220px;height:102px;background:var(--white);padding:12px 18px}
.phases .h-sec{color:var(--purple);font-size:9px;line-height:1.25;margin-bottom:5px}
/* back */
.back{background:var(--purple)}
.back .title{position:absolute;left:30px;top:262px;width:340px;font-size:23px;color:var(--white)}
.back .join{position:absolute;left:30px;top:378px;width:300px;color:var(--white)}
.back .join .h-sec{color:var(--yellow);font-size:13px;margin-bottom:6px}
.back .url{font-family:"Montserrat",sans-serif;font-weight:700;font-size:9px;color:var(--yellow);margin-top:8px}
</style>
</head>
<body>
<main class="sheet">

  <section class="page cover">
    <div class="photo tone-lab" style="left:0;top:0;width:400px;height:310px" role="img" aria-label="Photo of a female researcher working in a laboratory"></div>
    <svg class="deco" width="400" height="566" viewBox="0 0 400 566" aria-hidden="true">
      <path d="M0 322 Q200 252 400 292 L400 566 L0 566Z" fill="#fff"/>
      <path d="M0 308 Q200 238 400 278" fill="none" stroke="#f6b222" stroke-width="10"/>
      <path d="M0 294 Q200 224 400 264" fill="none" stroke="#4b3f9c" stroke-width="6"/>
      <path d="M250 566 Q330 500 400 470 L400 566Z" fill="#f6b222"/>
    </svg>
    <div class="brand" style="left:34px;top:346px;font-size:26px"><span class="dot"></span>BLENOX</div>
    <h1 class="h-title title">Joining Study and Progress for Fair Opportunity</h1>
    <div class="funding" style="left:34px;top:522px;width:200px"><span class="flag"></span>This project has received funding from a European research programme under grant agreement No 000000.</div>
  </section>

  <section class="page">
    <div class="photo tone-cool" style="left:0;top:0;width:400px;height:208px" role="img" aria-label="Photo of researchers using scientific equipment"></div>
    <div style="position:absolute;left:0;top:150px;width:170px;height:58px;background:var(--white)"></div>
    <div class="brand" style="left:22px;top:166px;font-size:22px"><span class="dot"></span>BLENOX</div>
    <div class="about">
      <h2 class="h-sec">About BLENOX</h2>
      <p class="copy">BLENOX brings together research and innovation organisations to design, apply and assess gender equality plans, helping to strengthen the position of women in STEM research across Europe.</p>
    </div>
    <div class="consortium">
      <h2 class="h-sec">The Consortium</h2>
      <p class="copy">Eleven partners from nine European countries, including universities, research centres and innovation agencies, share methods, tools and experience.</p>
      <div class="badges"><span></span><span></span><span></span><span></span><span></span><span></span><span></span><span></span><span></span><span></span></div>
    </div>
    <div class="goal-strip"></div>
    <div class="photo tone-warm" style="left:0;top:438px;width:200px;height:128px" role="img" aria-label="Photo of a young scientist at a lab bench"></div>
    <div class="goal">
      <h2 class="h-sec">The Goal</h2>
      <p class="copy">To support nine research organisations in setting up gender equality plans that bring lasting structural change.</p>
    </div>
  </section>

  <section class="page">
    <svg class="deco" width="400" height="566" viewBox="0 0 400 566" aria-hidden="true">
      <circle cx="340" cy="150" r="136" fill="#f6b222"/>
    </svg>
    <div class="photo tone-lab" style="left:212px;top:22px;width:256px;height:256px;border-radius:50%" role="img" aria-label="Photo of two researchers working with laboratory equipment"></div>
    <div class="hubs">
      <h2 class="h-sec">BLENOX Research &amp; Innovation Hubs</h2>
      <p class="copy">Each partner runs a Research &amp; Innovation Hub that gathers local stakeholders, shares good practice and keeps the change process alive beyond the project.</p>
    </div>
    <div class="impact">
      <h2 class="h-sec">Impact</h2>
      <p class="copy">BLENOX expects more balanced teams, fairer career paths and research content that takes gender into account.</p>
    </div>
    <h2 class="h-sec levels-head">The levels of institutional change</h2>
    <ul class="levels">
      <li><span class="ico"><svg width="14" height="14" viewBox="0 0 14 14"><path d="M2 7l3 3 7-7" fill="none" stroke="#f6b222" stroke-width="2"/></svg></span>Recruitment, retention and career progression</li>
      <li><span class="ico"><svg width="14" height="14" viewBox="0 0 14 14"><path d="M2 7h9M8 3l4 4-4 4" fill="none" stroke="#f6b222" stroke-width="2"/></svg></span>Work–life balance and organisational culture</li>
      <li><span class="ico"><svg width="14" height="14" viewBox="0 0 14 14"><path d="M2 12V7M7 12V3M12 12V5" fill="none" stroke="#f6b222" stroke-width="2"/></svg></span>Gender balance in leadership and decision-making</li>
      <li><span class="ico"><svg width="14" height="14" viewBox="0 0 14 14"><circle cx="7" cy="7" r="4.5" fill="none" stroke="#f6b222" stroke-width="2"/></svg></span>Gender dimension in research and teaching</li>
    </ul>
    <div class="photo tone-desk" style="left:0;top:464px;width:180px;height:102px" role="img" aria-label="Photo of a team meeting around a table seen from above"></div>
    <div class="phases">
      <h2 class="h-sec">Five phases of plan design and implementation</h2>
      <p class="copy">Audit · Plan · Implement · Monitor · Evaluate — a clear path from analysis to sustainable action.</p>
    </div>
    <div class="funding" style="left:198px;top:538px;width:190px"><span class="flag" style="width:22px;height:15px"></span></div>
  </section>

  <section class="page back">
    <div class="photo tone-warm" style="left:0;top:0;width:400px;height:240px" role="img" aria-label="Photo of a smiling female scientist in a laboratory"></div>
    <svg class="deco" width="400" height="566" viewBox="0 0 400 566" aria-hidden="true">
      <path d="M0 250 Q200 190 400 226 L400 566 L0 566Z" fill="#4b3f9c"/>
      <path d="M0 240 Q200 180 400 216" fill="none" stroke="#f6b222" stroke-width="8"/>
    </svg>
    <h2 class="h-title title">Joining Study and Progress for Fair Opportunity</h2>
    <div class="join">
      <h3 class="h-sec">Join BLENOX</h3>
      <p class="copy">Follow our news, events and results and get involved in the network.</p>
      <p class="url">https://blenox-project.example/</p>
    </div>
    <div class="funding" style="left:30px;top:516px;width:220px;color:var(--white)"><span class="flag"></span>This project has received funding from a European research programme under grant agreement No 000000.</div>
  </section>

</main>
</body>
</html>
```